Book Cover design

The book title is Rain falls slowly on quiet gardens

I need a book cover design for a book about the unexpected loss of child. The book is a journal of my first 12 months after the loss of my son. An expression of how the grief never ends you just learn to cope. The journey to healing and hope.
Updates

Change in book title

Target Market(s)

Anyone that has experienced loss of love, career, physical loss, PTSD or experienced losing someone in an untimely manner

Font styles to use
Serif

Colors
0456a4
0792cd
33b8a4
acd136
ffffff
cee9f5
cfdeed

Requirements
Must have
• Beauty Depth

```html
<!DOCTYPE html>
<html lang="en">
<head>
<meta charset="utf-8">
<title>Rain Falls Slowly on Quiet Gardens – Book Cover</title>
<link rel="stylesheet" href="https://fonts.googleapis.com/css2?family=Lora:wght@400;500&display=swap">
<style>
  :root {
    --stage-blue: #0456a4;
    --sky-blue: #0792cd;
    --deep-blue: #0a5fae;
    --teal: #33b8a4;
    --ice: #cee9f5;
    --white: #ffffff;
    --ink: #1a1a1a;
  }
  html, body {
    margin: 0;
    padding: 0;
    width: 1200px;
    height: 800px;
    overflow: hidden;
    background: var(--stage-blue);
  }
  .stage {
    position: relative;
    width: 1200px;
    height: 800px;
  }
  .book-cover {
    position: absolute;
    left: 400px;
    top: 40px;
    width: 400px;
    height: 720px;
    box-shadow: 0 18px 40px rgba(0, 0, 0, 0.35);
  }
  .book-cover svg { display: block; }
  .title-line {
    font-family: "Lora", serif;
    font-weight: 500;
    fill: var(--white);
  }
  .subtitle {
    font-family: "Lora", serif;
    fill: var(--ink);
  }
  .author-name {
    font-family: "Lora", serif;
    fill: var(--ink);
  }
</style>
</head>
<body>
<main class="stage">
  <div class="book-cover">
    <svg width="400" height="720" viewBox="0 0 400 720" xmlns="http://www.w3.org/2000/svg">
      <defs>
        <linearGradient id="left-quarter" x1="0" y1="0" x2="1" y2="0">
          <stop offset="0" stop-color="#06427f"/>
          <stop offset="1" stop-color="#0879c0"/>
        </linearGradient>
        <linearGradient id="right-quarter" x1="0" y1="1" x2="1" y2="0">
          <stop offset="0" stop-color="#0a5fae"/>
          <stop offset="1" stop-color="#6a9fd0"/>
        </linearGradient>
        <linearGradient id="top-quarter" x1="0" y1="0" x2="1" y2="0">
          <stop offset="0" stop-color="#0880c2"/>
          <stop offset="0.7" stop-color="#0792cd"/>
          <stop offset="1" stop-color="#5ab6de"/>
        </linearGradient>
        <radialGradient id="womb-glow" cx="0.5" cy="0.42" r="0.6">
          <stop offset="0" stop-color="#f6d9a8"/>
          <stop offset="0.45" stop-color="#8c6a8a"/>
          <stop offset="0.72" stop-color="#3b2a64"/>
          <stop offset="1" stop-color="#1f6fbf"/>
        </radialGradient>
        <filter id="title-shadow" x="-20%" y="-20%" width="140%" height="160%">
          <feDropShadow dx="3" dy="4" stdDeviation="2" flood-color="#000" flood-opacity="0.45"/>
        </filter>
      </defs>

      <g class="cover-quarters">
        <polygon points="0,0 400,0 200,242" fill="url(#top-quarter)"/>
        <polygon points="0,0 200,242 0,485" fill="url(#left-quarter)"/>
        <polygon points="400,0 400,485 200,242" fill="url(#right-quarter)"/>
        <polygon points="0,485 200,242 400,485" fill="var(--sky-blue)"/>
      </g>

      <g class="cover-cross" stroke="var(--ice)" stroke-width="5">
        <line x1="0" y1="0" x2="400" y2="485"/>
        <line x1="400" y1="0" x2="0" y2="485"/>
      </g>

      <g class="cover-medallion">
        <circle cx="200" cy="262" r="122" fill="url(#womb-glow)" stroke="var(--ink)" stroke-width="3"
                role="img" aria-label="Illustration of an unborn baby curled inside a softly glowing womb"/>
      </g>

      <g class="book-title" filter="url(#title-shadow)">
        <text class="title-line" x="200" y="64" font-size="27" text-anchor="middle"
              textLength="300" lengthAdjust="spacing">RAIN FALLS SLOWLY</text>
        <text class="title-line" x="200" y="112" font-size="27" text-anchor="middle"
              textLength="350" lengthAdjust="spacing">ON QUIET GARDENS</text>
      </g>

      <text class="subtitle" x="200" y="470" font-size="18" text-anchor="middle">...the journey to healing and hope</text>

      <rect class="author-band" x="0" y="485" width="400" height="235" fill="var(--teal)"/>
      <text class="author-name" x="200" y="640" font-size="36" text-anchor="middle">Author Name</text>
    </svg>
  </div>
</main>
</body>
</html>
```